VOSKE - New website for high-quality knives, aprons, chopping boards and caps for Grillers

We would like to develop a new website for our brand-new outdoor cooking brand VOSKE. VOSKE is a brand by grillers for grillers. Therefore the griller will always be in the centre of everything that we do. We want to appear as a cool, robust brand without being too stereotypical (like any other BBQ brands (so not too much black, red, flames)). We're very international and that should also come back in the design.

Main colour will be the yellow supported by red white and black. However, we're also open to other colours

VOSKE will be sold in-store but we want to provide more information to our clients via the website. This will be done through detailed descriptions but also blogs and downloads. We will work together with influencers to share recipes in our Pavane (magazine) and on our blog page.

Website needs to be responsive (web+mobile) and our own team should be able to easily add new content to the website.

Target Market(s)

International grillers or home chefs

Industry/Entity Type

BBQ and outdoor cooking

Coding

Coded - Design and coding required

Other font styles liked:
• Allan & Cambria

Colors

Designer to choose colors to be used in the design.

Requirements
Must have
• home, products (not shop), blog, contact, socials, downloads (for Pavane).
Nice to have
• instagram grid with #voske
Should not have
• too stereotypical BBQ website (red, flames, black)

```html
<!DOCTYPE html>
<html lang="en">
<head>
<meta charset="utf-8">
<title>VOSKE – Gear for Grillers</title>
<link rel="stylesheet" href="https://fonts.googleapis.com/css2?family=Allan:wght@700&family=Caladea:ital,wght@0,400;0,700;1,400&family=Lato:wght@400&display=swap">
<style>
:root{
  --yellow:#f5a623;
  --red:#c8102e;
  --ink:#1e1e1e;
  --text:#333333;
  --white:#ffffff;
  --mist:#f3f3f3;
  --footer:#1b1b1b;
  --display:"Allan", cursive;
  --serif:"Caladea", Georgia, serif;
}
*{margin:0;padding:0;box-sizing:border-box}
html,body{width:1200px;height:3213px;overflow:hidden;background:var(--white)}
body{position:relative;font-family:var(--serif);color:var(--text)}
.abs{position:absolute}
.center{left:0;width:1200px;text-align:center}

/* header */
.site-header{position:absolute;left:0;top:0;width:1200px;height:104px;background:var(--white);z-index:3}
.nav-link{position:absolute;top:43px;font:700 17px/22px var(--serif);letter-spacing:.5px;color:var(--ink);text-transform:uppercase}
.nav-link.is-accent{color:var(--red)}
.brand-badge{position:absolute;left:518px;top:18px;width:164px;height:164px;border-radius:50%;background:var(--yellow);border:9px solid var(--white);z-index:4;display:flex;align-items:center;justify-content:center;font:700 38px/1 var(--serif);color:var(--white);letter-spacing:1px}

/* hero */
.hero{position:absolute;left:0;top:104px;width:1200px;height:694px;background:linear-gradient(180deg,#2f3d22 0%,#4a5a2c 45%,#3b4824 75%,#1f2416 100%)}
.hero-title{top:338px;font:700 88px/1 var(--display);font-style:italic;color:var(--white);text-transform:uppercase;letter-spacing:1px}
.hero-sub{top:430px;font:700 40px/49px var(--display);font-style:italic;color:var(--white)}

.btn{position:absolute;height:60px;background:var(--yellow);color:var(--white);font:700 30px/60px var(--display);font-style:italic;text-align:center}

.section-title{font:700 48px/1 var(--display);font-style:italic;color:var(--ink);text-transform:uppercase}
.intro{top:940px;font:400 19px/36px var(--serif);color:var(--text)}

/* products */
.products-panel{position:absolute;left:0;top:1206px;width:405px;height:544px;background:#242424}
.products-panel h2{position:absolute;top:66px;left:0;width:405px;text-align:center;font:700 46px/1 var(--display);font-style:italic;color:var(--white);text-transform:uppercase}
.products-panel p{position:absolute;top:132px;left:50px;width:305px;text-align:center;font:400 18px/36px var(--serif);color:#e6e6e6}
.tile{position:absolute;width:333px;height:259px}
.tile-label{position:absolute;left:0;bottom:18px;width:100%;text-align:center;font:700 33px/1 var(--serif);color:var(--white);letter-spacing:.5px}

/* blog */
.post{position:absolute;top:1897px;width:331px}
.post-image{width:331px;height:267px}
.post-tab{position:relative;margin:-34px auto 0;width:295px;height:34px;background:var(--white)}
.post-date{position:absolute;left:0;top:14px;width:100%;text-align:center;font:700 19px/1 var(--display);font-style:italic;color:var(--red)}
.post-title{margin-top:6px;text-align:center;font:400 27px/33px var(--serif);color:var(--ink)}
.post-excerpt{margin-top:6px;text-align:center;font:400 16px/27px var(--serif);color:var(--text)}

/* subscribe */
.subscribe{position:absolute;left:0;top:2495px;width:1200px;height:362px;background:var(--mist)}
.email-field{position:absolute;left:287px;top:2731px;width:415px;height:62px;background:var(--white);border:1px solid #c9c9c9;padding-left:18px;font:400 italic 18px/60px var(--display);color:#555}

/* footer */
.site-footer{position:absolute;left:0;top:2857px;width:1200px;height:356px;background:var(--footer)}
.footer-badge{position:absolute;left:77px;top:2941px;width:150px;height:150px;border-radius:50%;background:var(--yellow);display:flex;align-items:center;justify-content:center;font:700 34px/1 var(--serif);color:var(--white);letter-spacing:1px}
.footer-col{position:absolute;top:2908px}
.footer-col h3{font:700 19px/22px var(--serif);color:var(--yellow);letter-spacing:.5px;text-transform:uppercase;margin-bottom:8px}
.footer-col li{list-style:none;font:400 17px/31px var(--serif);color:#e2e2e2;letter-spacing:.4px}
.footer-col li.pair{line-height:27px;margin-bottom:8px}
.copyright{position:absolute;left:77px;top:3174px;font:400 13px/16px "Lato", sans-serif;color:#e2e2e2}
.social-dot{position:absolute;top:3170px;width:22px;height:22px;border-radius:50%;border:2px solid var(--white)}
</style>
</head>
<body>

<header class="site-header">
  <a class="nav-link" style="left:115px">Home</a>
  <a class="nav-link" style="left:215px">Products</a>
  <a class="nav-link" style="left:357px">Blog</a>
  <a class="nav-link" style="left:762px">Contact</a>
  <a class="nav-link" style="left:890px">Socials</a>
  <a class="nav-link is-accent" style="left:1010px">Downloads</a>
</header>
<div class="brand-badge">VOSKE</div>

<section class="hero" role="img" aria-label="Photo of a griller in an apron placing meat on a kamado grill in a green garden"></section>
<h1 class="abs center hero-title">Welcome to VOSKE</h1>
<p class="abs center hero-sub">We Sell high-quality knives, aprons, chopping boards<br>and caps for Grillers.</p>
<a class="btn" style="left:496px;top:551px;width:208px">Read More</a>

<h2 class="abs center section-title" style="top:870px">Who are we?</h2>
<p class="abs center intro">VOSKE is by the grillers for the grillers. Premium quality products to ato ensure a pleasant experience.<br>VOSKE is specialized in knives, caps,sunglasses, sauces and much more. VOSKE is for everyone who loves lifeenjoy<br>and love cool products that are refined and good in quality.</p>
<a class="btn" style="left:496px;top:1076px;width:208px">Read More</a>

<section class="products-panel" role="img" aria-label="Dark photo of grilling tools behind the products introduction">
  <h2>Products</h2>
  <p>Sed ut perspiciatis unde omnis iste natus error sit voluptatem accusantium doloremque laudantium, totam rem aperiam, eaque ipsa quae ab illo inventore veritatis et quasi architecto beatae vitae dicta sunt explicabo.</p>
</section>
<a class="btn" style="left:99px;top:1622px;width:207px">Read More</a>

<div class="tile" style="left:434px;top:1206px;background:linear-gradient(180deg,#3d5a2a 0%,#2c3a4a 45%,#4a3526 80%,#1d1d1d 100%)" role="img" aria-label="Photo of a leather knife roll with chef knives on a wooden board"><span class="tile-label">Knives</span></div>
<div class="tile" style="left:793px;top:1206px;background:linear-gradient(180deg,#3a3532 0%,#262322 60%,#151414 100%)" role="img" aria-label="Photo of a black leather apron close-up"><span class="tile-label">Aprons</span></div>
<div class="tile" style="left:434px;top:1491px;background:linear-gradient(180deg,#2f3a26 0%,#5a3a26 50%,#2a1e18 100%)" role="img" aria-label="Photo of meat being sliced on a chopping board with asparagus"><span class="tile-label">Chopping Boards</span></div>
<div class="tile" style="left:793px;top:1491px;background:linear-gradient(180deg,#c9c9c9 0%,#8c8c8c 50%,#2b2b2b 100%)" role="img" aria-label="Photo of a grey cap held in hand"><span class="tile-label">Caps</span></div>

<h2 class="abs center section-title" style="top:1818px">Blog</h2>

<article class="post" style="left:75px">
  <div class="post-image" role="img" aria-label="Photo of a griller plating food beside a kamado grill" style="background:linear-gradient(180deg,#3b4a2a 0%,#2b3550 50%,#4a3422 100%)"></div>
  <div class="post-tab"><span class="post-date">SEP 25, 2021</span></div>
  <h3 class="post-title">Nemo enim ipsam voluptatem quia voluptas</h3>
  <p class="post-excerpt">Neque porro quisquam est, qui dolorem ipsum quia dolor sit amet, consectetur, adipisci velit.</p>
</article>
<article class="post" style="left:434px">
  <div class="post-image" role="img" aria-label="Photo of friends toasting with wine at an outdoor dinner table" style="background:linear-gradient(180deg,#4a5a3a 0%,#6a5a4a 50%,#3a3230 100%)"></div>
  <div class="post-tab"><span class="post-date">SEP 25, 2021</span></div>
  <h3 class="post-title">Nemo enim ipsam voluptatem quia voluptas</h3>
  <p class="post-excerpt">Neque porro quisquam est, qui dolorem ipsum quia dolor sit amet, consectetur, adipisci velit.</p>
</article>
<article class="post" style="left:796px">
  <div class="post-image" role="img" aria-label="Photo of a blue kamado grill with a leather knife roll in front" style="background:linear-gradient(180deg,#6a7a6a 0%,#23344e 45%,#1e2c44 75%,#8a6448 100%)"></div>
  <div class="post-tab"><span class="post-date">SEP 25, 2021</span></div>
  <h3 class="post-title">Nemo enim ipsam voluptatem quia voluptas</h3>
  <p class="post-excerpt">Neque porro quisquam est, qui dolorem ipsum quia dolor sit amet, consectetur, adipisci velit.</p>
</article>

<a class="btn" style="left:496px;top:2386px;width:208px">View All Blog</a>

<section class="subscribe"></section>
<h2 class="abs center section-title" style="top:2658px">Email Subscribe</h2>
<div class="email-field">Email Address</div>
<a class="btn" style="left:710px;top:2731px;width:207px;height:62px;line-height:62px">Subscribe</a>

<footer class="site-footer"></footer>
<div class="footer-badge">VOSKE</div>
<div class="footer-col" style="left:343px">
  <h3>Site Map</h3>
  <ul><li>Home</li><li>Products</li><li>Blog</li><li>Contact</li><li>Socials</li><li>Downloads</li></ul>
</div>
<div class="footer-col" style="left:595px">
  <h3>Contact Us</h3>
  <ul><li class="pair">Sed ut perspiciatis unde<br>omnis iste natus</li><li>1-800-555-0142</li><li>info@voskegrill.com</li></ul>
</div>
<div class="footer-col" style="left:914px">
  <h3>Support</h3>
  <ul><li>Sed ut perspiciatis</li><li>Unde omnis iste</li><li>Natus error</li><li>Nemo enim ipsam</li></ul>
</div>
<p class="copyright">Copyright © 2021. VOSKE Outdoor Co. All Right Reserved</p>
<span class="social-dot" style="left:920px" aria-label="Social link"></span>
<span class="social-dot" style="left:962px" aria-label="Social link"></span>
<span class="social-dot" style="left:1007px" aria-label="Social link"></span>
<span class="social-dot" style="left:1057px" aria-label="Social link"></span>
<span class="social-dot" style="left:1102px" aria-label="Social link"></span>

</body>
</html>
```